Stonewell Holdings

Professional looking business card using darker colours
I do not yet have a logo for the company so feel free to suggest
The business is based on consultancy and project management
Based in Melbourne
Business card can omit the word "Holdings" and can be Stonewell consulting etc.

Contact Name on card : Ravi Pelunkoda Contact number : +61433 512 604 Email address will be confirmed shortly.

```html
<!DOCTYPE html>
<html lang="en">
<head>
<meta charset="utf-8">
<title>Stonewell — business card</title>
<link href="https://fonts.googleapis.com/css2?family=Lexend:wght@300;400;600&display=swap" rel="stylesheet">
<style>
  :root {
    --navy: #1d3664;
    --grey: #a7a7a7;
    --white: #ffffff;
    --stage: #ece5d8;
    --shadow: rgba(40, 30, 15, 0.35);
  }
  * { box-sizing: border-box; margin: 0; padding: 0; }
  html, body {
    width: 1189px; height: 1200px; overflow: hidden;
    background: var(--stage);
  }
  .canvas { position: relative; width: 1189px; height: 1200px; }

  .card {
    position: absolute; left: 171px; width: 856px; height: 487px;
    border-radius: 20px; overflow: hidden;
    box-shadow: 4px 8px 14px var(--shadow);
  }
  .card--front { top: 68px; background: var(--navy); }
  .card--back { top: 627px; background: var(--white); }

  .wordmark {
    position: absolute; text-align: center;
    font-family: "Lexend", sans-serif; font-weight: 400;
    line-height: 1; letter-spacing: -0.5px;
  }
  .card--front .wordmark {
    left: 0; right: 0; top: 300px;
    font-size: 60px; color: var(--white);
  }
  .card--back .wordmark {
    left: 470px; width: 330px; top: 281px;
    font-size: 56px; color: var(--navy);
  }

  .back-panel { position: absolute; inset: 0; width: 856px; height: 487px; }

  .contact {
    position: absolute; left: 43px; top: 90px;
    font-family: "Lexend", sans-serif; color: var(--white);
  }
  .contact__name { font-size: 30px; font-weight: 600; line-height: 1.05; letter-spacing: -0.3px; }
  .contact__role { font-size: 20px; font-weight: 300; line-height: 1.1; }
  .contact__address { margin-top: 48px; font-size: 22px; font-weight: 300; line-height: 1.3; }
  .contact__lines { margin-top: 18px; font-size: 22px; font-weight: 300; line-height: 1.15; list-style: none; }
  .contact__lines li { display: flex; align-items: center; gap: 19px; }
  .contact__icon { width: 20px; height: 20px; flex: none; }
  .contact__web { margin-top: 24px; font-size: 21px; font-weight: 300; }
</style>
</head>
<body>
<main class="canvas">

  <section class="card card--front" aria-label="Card front">
    <p class="wordmark">Stonewell</p>
  </section>

  <section class="card card--back" aria-label="Card back">
    <svg class="back-panel" viewBox="0 0 856 487" aria-hidden="true">
      <path d="M0 0 H432 Q356 243 432 487 H0 Z" fill="var(--grey)"/>
      <path d="M0 0 H428 Q334 243 428 487 H0 Z" fill="var(--white)"/>
      <path d="M0 0 H425 Q326 243 425 487 H0 Z" fill="var(--navy)"/>
    </svg>

    <div class="contact">
      <p class="contact__name">Ravi Pelunkoda</p>
      <p class="contact__role">Director</p>
      <p class="contact__address">Stonewell Office<br>Ave Carlton, VIC 3053</p>
      <ul class="contact__lines">
        <li>
          <svg class="contact__icon" viewBox="0 0 20 20" aria-label="Phone">
            <rect width="20" height="20" rx="4" fill="var(--white)"/>
            <rect x="7" y="3.5" width="6" height="13" rx="1.2" fill="var(--navy)"/>
            <rect x="8.2" y="5" width="3.6" height="3" fill="var(--white)"/>
          </svg>
          <span>+61433 512 604</span>
        </li>
        <li>
          <svg class="contact__icon" viewBox="0 0 20 20" aria-label="Email">
            <rect width="20" height="20" rx="4" fill="var(--white)"/>
            <rect x="4" y="6" width="12" height="8.5" fill="none" stroke="var(--navy)" stroke-width="1.4"/>
            <path d="M4 6 L10 11 L16 6 M4 14.5 L8.5 10 M16 14.5 L11.5 10" fill="none" stroke="var(--navy)" stroke-width="1.2"/>
          </svg>
          <span>hello@stonewell.net.au</span>
        </li>
      </ul>
      <p class="contact__web">www.stonewellconsult.com</p>
    </div>

    <p class="wordmark">Stonewell</p>
  </section>

</main>
</body>
</html>
```